Korvane Pty Ltd professional business card

A professional business card template using the colours from the supplied logo.
Clean crisp lines while, Modern while not being over the top.

Target Market(s)

Construction, commerical and industrial

Industry/Entity Type

Communications

Contact Information for Business Card

For a Communications, IT, Optical fibre installation company

Colors
37b8a4

```html
<!DOCTYPE html>
<html lang="en">
<head>
<meta charset="utf-8">
<title>Korvane Pty Ltd – Business Card</title>
<link rel="stylesheet" href="https://fonts.googleapis.com/css2?family=Montserrat:wght@400;500;700&display=swap">
<style>
  :root {
    --teal: #1e93a0;
    --grey: #6d6e71;
    --silver: #b9bcbf;
    --white: #ffffff;
    --stage: #2a2a2a;
  }
  * { box-sizing: border-box; margin: 0; padding: 0; }
  html, body {
    width: 1200px; height: 900px; overflow: hidden;
    background: var(--stage);
    font-family: "Montserrat", Arial, sans-serif;
  }
  .card {
    position: absolute; left: 250px;
    width: 700px; height: 400px; overflow: hidden;
  }
  .card-front { top: 25px; background: var(--teal);
    display: flex; align-items: center; justify-content: center; }
  .card-back { top: 475px; background: var(--white); }
  .wordmark {
    font-weight: 500; letter-spacing: 4px; line-height: 1;
  }
  .card-front .wordmark { color: var(--silver); font-size: 78px; }
  .card-back .wordmark {
    position: absolute; left: 48px; top: 40px;
    color: var(--grey); font-size: 50px;
  }
  .band { position: absolute; inset: 0; }
  .person { position: absolute; left: 52px; top: 122px; }
  .person-name { color: var(--teal); font-weight: 700; font-size: 23px; letter-spacing: 1px; }
  .person-role { color: var(--grey); font-size: 18px; margin-top: 2px; letter-spacing: 0.5px; }
  .divider { position: absolute; left: 50px; top: 186px; width: 270px; height: 1.5px; background: var(--grey); }
  .contacts {
    position: absolute; left: 50px; top: 242px; list-style: none;
    color: var(--white); font-size: 18px; line-height: 27px;
  }
  .contacts li { display: flex; align-items: center; gap: 10px; }
  .contacts svg { width: 18px; height: 18px; flex: none; }
</style>
</head>
<body>
  <section class="card card-front" aria-label="Card front">
    <div class="wordmark">KORVANE</div>
  </section>

  <section class="card card-back" aria-label="Card back">
    <svg class="band" viewBox="0 0 700 400" preserveAspectRatio="none" aria-hidden="true">
      <polygon points="0,198 700,300 700,400 0,400" fill="var(--teal)"/>
    </svg>
    <div class="wordmark">KORVANE</div>
    <div class="person">
      <div class="person-name">MARCUS ELLERY</div>
      <div class="person-role">Project Manager</div>
    </div>
    <div class="divider"></div>
    <ul class="contacts">
      <li>
        <svg viewBox="0 0 20 20" fill="none" stroke="currentColor" stroke-width="1.5"><circle cx="10" cy="10" r="8.5"/><path d="M7 5.5l1.6 2.2-1 1.2c.6 1.3 1.7 2.4 3 3l1.2-1 2.2 1.6-.8 1.6c-3.4-.2-6.9-3.7-7.1-7.1z"/></svg>
        555 018 2047
      </li>
      <li>
        <svg viewBox="0 0 20 20" fill="none" stroke="currentColor" stroke-width="1.5"><rect x="2" y="4.5" width="16" height="11"/><path d="M2 4.5l8 6 8-6"/></svg>
        marcus@korvaneptyltd.com
      </li>
      <li>
        <svg viewBox="0 0 20 20" fill="none" stroke="currentColor" stroke-width="1.5"><circle cx="10" cy="10" r="8"/><ellipse cx="10" cy="10" rx="3.5" ry="8"/><path d="M2 10h16M3.5 6h13M3.5 14h13"/></svg>
        www.korvaneptyltd.com
      </li>
      <li>PoBox 48213, Sydney. AU</li>
      <li>
        <svg viewBox="0 0 20 20" fill="none" stroke="currentColor" stroke-width="1.6"><circle cx="10" cy="10" r="7.5"/></svg>
        @korvanecomms
      </li>
    </ul>
  </section>
</body>
</html>
```